Web Design - RN Fieldline Supply

RN Fieldline Supply is a future eCommerce wholesaler and retailer for tactical equipment such as: bulletproof vests, protective armor plates, ballistic helmets, military uniforms, magazines, military backpacks, etc. our main market will be the U.S market; U.S military, law enforcement and police. You can find the website on www.rnfieldlineshop.com – I’m using a magento template but definitely need to customize the design. A clean and strong design is required and it also needs to incorporate eCommerce color scheme to highlight the important fields; BUY, SHOP, etc.

Please review the attached file to see our logo and incorporate the same style and colors

For exemple:
• http://www.738outfitrow.com/
• http://www.pmwguardworksco.com/
• http://www.tolvanexacta.com/
• http://www.nimbraloftkit.com/
• http://www.vrnopsline.com/
Thanks

Target Market(s)

U.S Military, U.S. Law Enforcement, Police

Industry/Entity Type

Shop

Requirements
Must have
• Home page must have a rotating / revolving banner with U.S Military / U.S Law Enforcement special forces / SWAT / ONQ pictures in battlefield - at least 3-4 banners

```html
<!DOCTYPE html>
<html lang="en">
<head>
<meta charset="utf-8">
<title>RN Fieldline Supply – Home</title>
<link rel="stylesheet" href="https://fonts.googleapis.com/css2?family=Open+Sans:wght@400;600;700&family=Oswald:wght@500;600&display=swap">
<style>
:root{
  --bg-dark:#232323;
  --bg-darker:#151515;
  --footer:#1c1c1c;
  --panel:#ffffff;
  --panel-border:#cfcfcf;
  --orange:#f5a01a;
  --orange-deep:#e07f0c;
  --text-dark:#222222;
  --text-muted:#7a7a7a;
  --link-light:#cfcfcf;
  --white:#ffffff;
}
*{box-sizing:border-box;margin:0;padding:0}
html,body{width:882px;height:1200px;overflow:hidden}
body{
  position:relative;
  background:radial-gradient(ellipse at 50% 30%,#2f2f2f 0%,var(--bg-dark) 55%,#1a1a1a 100%);
  font-family:"Open Sans",Arial,sans-serif;
  color:var(--text-dark);
}
ul{list-style:none}

/* Utility bar */
.utility{position:absolute;top:8px;right:28px;display:flex;align-items:center;gap:8px;font-size:9.5px;color:var(--link-light)}
.utility .sep{color:#666}
.cart-btn{background:var(--orange);color:var(--white);font-weight:700;padding:3px 8px;border-radius:2px;display:flex;align-items:center;gap:4px}

/* Brand */
.brand{position:absolute;left:52px;top:50px;display:flex;align-items:center;gap:12px}
.brand-mark{width:36px;height:36px;background:var(--orange)}
.brand-name{font-family:"Oswald",Arial,sans-serif;font-weight:600;font-size:27px;color:var(--white);letter-spacing:.5px}

/* Search */
.search{position:absolute;left:706px;top:50px;width:145px;height:22px;background:#3a3a3a;border:1px solid #555;border-radius:2px;font-size:9px;color:#999;padding:4px 8px;display:flex;justify-content:space-between;align-items:center}

/* Main navigation */
.main-nav{position:absolute;right:44px;top:90px;display:flex;font-family:"Oswald",Arial,sans-serif;font-weight:500;font-size:13px}
.main-nav a{color:var(--white);text-decoration:none;padding:6px 11px;display:block}
.main-nav a.active{background:var(--orange)}

/* Content panel */
.panel{position:absolute;left:44px;top:123px;width:794px;height:762px;background:var(--panel);border:1px solid var(--panel-border)}
.hero{position:absolute;left:10px;top:10px;width:774px;height:352px;
  background:linear-gradient(160deg,#c9cdd2 0%,#6b727a 35%,#2c3137 70%,#1a1d21 100%)}
.hero-dots{position:absolute;left:50%;bottom:14px;transform:translateX(-50%);display:flex;gap:6px}
.hero-dots span{width:8px;height:8px;border-radius:50%;background:rgba(255,255,255,.5)}
.hero-dots span.on{background:var(--white)}

.promo-strip{position:absolute;left:10px;top:362px;width:774px;height:44px;
  background:linear-gradient(180deg,#fbb73a 0%,var(--orange) 55%,var(--orange-deep) 100%);
  display:flex;align-items:center;padding-left:90px}
.promo-text{font-weight:700;font-size:12.5px;color:var(--white);text-transform:uppercase;letter-spacing:.2px}
.promo-btn{position:absolute;left:616px;top:9px;background:#1b1b1b;color:var(--white);font-weight:700;font-size:10.5px;padding:7px 14px;border-radius:2px}
.promo-arrows{position:absolute;right:12px;top:14px;display:flex;gap:8px}

.product{position:absolute;top:437px;width:240px}
.product-media{width:240px;height:155px}
.product h3{margin-top:14px;font-size:11.5px;font-weight:700;text-transform:uppercase;color:var(--text-dark)}
.product p{margin-top:6px;font-size:9.5px;line-height:1.45;color:var(--text-muted)}
.view-more{margin-top:14px;display:inline-block;background:var(--orange);color:var(--white);font-weight:700;font-size:9.5px;padding:5px 10px;border-radius:2px}

/* Footer */
.site-footer{position:absolute;left:0;top:905px;width:882px;height:265px;background:var(--footer);border-top:3px solid #2c2c2c}
.footer-col{position:absolute;top:22px}
.footer-col h4{font-family:"Oswald",Arial,sans-serif;font-weight:500;font-size:13px;color:var(--orange);margin-bottom:10px}
.footer-col li{font-size:9.5px;color:var(--link-light);line-height:19px}
.footer-col .sub{position:absolute;top:26px}
.social{display:flex;gap:8px}
.social span{width:22px;height:22px;border-radius:50%;background:#4a4a4a}
.footer-brand{margin-top:40px;display:flex;align-items:center;gap:8px}
.footer-brand .brand-mark{width:24px;height:24px}
.footer-brand .brand-name{font-size:17px}
.legal{position:absolute;left:0;top:1170px;width:882px;height:30px;background:var(--bg-darker);font-size:9px;color:#9a9a9a;padding:9px 64px}
</style>
</head>
<body>

<div class="utility">
  <span>My Account</span><span class="sep">|</span>
  <span>Wish List</span><span class="sep">|</span>
  <span>Checkout</span><span class="sep">|</span>
  <span>Login</span>
  <span class="cart-btn">
    <svg width="10" height="9" viewBox="0 0 10 9"><path d="M0 1h2l1.5 5h5L10 2H3" fill="none" stroke="#fff" stroke-width="1.2"/><circle cx="4" cy="8" r="1" fill="#fff"/><circle cx="8" cy="8" r="1" fill="#fff"/></svg>
    0 items
  </span>
</div>

<header class="brand">
  <span class="brand-mark"></span>
  <span class="brand-name">RN Fieldline Supply</span>
</header>

<div class="search">
  <span>Search here...</span>
  <svg width="9" height="9" viewBox="0 0 10 10"><circle cx="4" cy="4" r="3" fill="none" stroke="#bbb" stroke-width="1.4"/><path d="M6.3 6.3 9 9" stroke="#bbb" stroke-width="1.4"/></svg>
</div>

<nav class="main-nav">
  <a class="active">HOME</a>
  <a>ABOUT</a>
  <a>CUSTOMER SERVICES</a>
  <a>PRODUCTS</a>
  <a>SITEMAP</a>
  <a>CONTACT</a>
</nav>

<main class="panel">
  <div class="hero" role="img" aria-label="Rotating banner: armed tactical team in helmets and gear">
    <div class="hero-dots"><span class="on"></span><span></span><span></span><span></span></div>
  </div>

  <div class="promo-strip">
    <span class="promo-text">Selling bulletproof vests protective armor plates ballistic helmets...</span>
    <span class="promo-btn">VIEW PRODUCT</span>
    <span class="promo-arrows">
      <svg width="12" height="16" viewBox="0 0 12 16"><path d="M10 1 3 8l7 7" fill="none" stroke="#3a2a10" stroke-width="3"/></svg>
      <svg width="12" height="16" viewBox="0 0 12 16"><path d="M2 1l7 7-7 7" fill="none" stroke="#3a2a10" stroke-width="3"/></svg>
    </span>
  </div>

  <article class="product" style="left:10px">
    <div class="product-media" role="img" aria-label="Operator in tactical vest" style="background:linear-gradient(135deg,#d9dde2,#6f7780 60%,#30353b)"></div>
    <h3>Nunc tempus felis vitae urna</h3>
    <p>Rugged gear tested in the field for patrol teams and units. Built to hold up under pressure and ready to ship fast to your door.</p>
    <span class="view-more">VIEW MORE ›</span>
  </article>

  <article class="product" style="left:277px">
    <div class="product-media" role="img" aria-label="Rows of rifle cartridges" style="background:linear-gradient(135deg,#5a3d1c,#b88a3e 50%,#2a1d10)"></div>
    <h3>Maecenas aliquet velit vel</h3>
    <p>Rugged gear tested in the field for patrol teams and units. Built to hold up under pressure and ready to ship fast to your door.</p>
    <span class="view-more">VIEW MORE ›</span>
  </article>

  <article class="product" style="left:544px">
    <div class="product-media" role="img" aria-label="Folded flag with camouflage uniform" style="background:linear-gradient(135deg,#c7ccd6,#8a8f84 45%,#4b4f47)"></div>
    <h3>Delivery best protection product</h3>
    <p>Rugged gear tested in the field for patrol teams and units. Built to hold up under pressure and ready to ship fast to your door.</p>
    <span class="view-more">VIEW MORE ›</span>
  </article>
</main>

<footer class="site-footer">
  <div class="footer-col" style="left:64px;width:250px">
    <h4>INFORMATION</h4>
    <ul>
      <li>About Us</li><li>Customer Service</li><li>Privacy Policy</li>
      <li>Site Map</li><li>Search Terms</li><li>Advanced Search</li>
    </ul>
    <ul class="sub" style="left:128px">
      <li>Orders and Returns</li><li>Contact Us</li><li>Request RMA</li>
    </ul>
  </div>
  <div class="footer-col" style="left:336px">
    <h4>WHY BUY FROM US</h4>
    <ul>
      <li>Shipping &amp; Returns</li><li>Secure Shopping</li><li>International Shipping</li>
      <li>Affiliates</li><li>Group Sales</li><li>My Cart</li>
    </ul>
  </div>
  <div class="footer-col" style="left:512px">
    <h4>MY ACCOUNT</h4>
    <ul>
      <li>Sign In</li><li>View Cart</li><li>My Wishlist</li>
      <li>Track My Order</li><li>Help</li><li>Support</li>
    </ul>
  </div>
  <div class="footer-col" style="left:668px">
    <h4>GET CONNECTED</h4>
    <div class="social"><span></span><span></span><span></span><span></span><span></span></div>
    <div class="footer-brand">
      <span class="brand-mark"></span>
      <span class="brand-name">RN Fieldline Supply</span>
    </div>
  </div>
</footer>

<div class="legal">© 2013 Company Name &nbsp;|&nbsp; Terms of Use &nbsp;|&nbsp; Policy Privacy</div>

</body>
</html>
```